Specialized tax accounting firm needs marketing postcard

We need a postcard design for a professional services firm called R. Desmond Plork Inc. The firm is essentially a very specialized tax accounting firm - instead of serving the end consumer, we support other public accounting firms in the area of Canadian and U.S. tax advisory and compliance (i.e. they call us on tax issues too complex for the general practitioner). Our byline is "Tax Support Services for Public Accounting Firms". Our postcard should utilize our logo and be based on colours present in our logo (see file attached). The final design needs to convey professionalism and trustworthiness (we're hired by accountants after all!) while being creative and eye-catching. Eye-catching is critical, since many prospective recipients will not have heard from me before and I want them to read the postcard.

I've attached:
The font used in the logo
The logo itself in a variety of file formats
A picture of myself for incorporation in the postcard
A sample postcard from Publisher showing the wording to be used in the postcard and the elements to be included

Please note that in including a draft postcard I don't want the designer to follow the layout as is. It just shows the basic elements I want included. The only element which should remain constant is the wording - I do want the text elements included as written - however, everything else - font, size, placement of elements, etc. is up for creative ideas.

Please note that there is much more leather background around the logo than needs to be incorporated in the letterhead.

Industry/Entity Type

Accounting

```html
<!DOCTYPE html>
<html lang="en">
<head>
<meta charset="utf-8">
<title>R. Desmond Plork Inc. — Postcard</title>
<link href="https://fonts.googleapis.com/css2?family=Cinzel:wght@400;600&family=Cormorant+Garamond:wght@500&family=Libre+Baskerville&family=Questrial&display=swap" rel="stylesheet">
<style>
  :root {
    --ink: #1a1a1a;
    --leather-dark: #141414;
    --leather-mid: #2c2c2c;
    --brand-orange: #f5a52a;
    --brand-blue: #1f7fc4;
    --paper: #ffffff;
    --label: #555555;
    --rule: #9a9a9a;
  }
  * { margin: 0; padding: 0; box-sizing: border-box; }
  html, body { width: 1200px; height: 1173px; overflow: hidden; background: var(--paper); }
  .canvas { position: relative; width: 1200px; height: 1173px; }

  .side-label {
    position: absolute; left: 241px;
    font-family: "Questrial", sans-serif; font-size: 24px; color: var(--label); line-height: 1;
  }
  .side-label.front-label { top: 26px; }
  .side-label.back-label { top: 604px; }

  .card-front {
    position: absolute; left: 241px; top: 51px; width: 711px; height: 551px;
    background: radial-gradient(ellipse at 70% 40%, var(--leather-mid), var(--leather-dark) 75%);
    border: 1px solid #000; overflow: hidden;
  }
  .card-front .portrait-art { position: absolute; inset: 0; }

  .brand { position: absolute; display: flex; align-items: center; gap: 10px; color: var(--paper); }
  .brand .brand-square { width: 50px; height: 50px; border: 3px solid var(--brand-orange); flex: none; }
  .brand .brand-text { font-family: "Cinzel", serif; text-align: center; width: 310px; }
  .brand .brand-name { font-size: 28px; letter-spacing: 1px; line-height: 1.1; white-space: nowrap; }
  .brand .brand-inc {
    display: flex; align-items: center; gap: 8px; font-size: 12px; letter-spacing: 2px; line-height: 1.1;
  }
  .brand .brand-inc::before, .brand .brand-inc::after { content: ""; flex: 1; height: 1px; background: var(--paper); }
  .brand .brand-byline { font-size: 8.6px; letter-spacing: 1px; white-space: nowrap; }
  .card-front .brand { left: 311px; top: 45px; }

  .front-headline {
    position: absolute; left: 317px; top: 143px; width: 380px;
    font-family: "Cinzel", serif; font-weight: 400; font-size: 21px; line-height: 26px; color: var(--paper); letter-spacing: .5px;
  }
  .front-copy {
    position: absolute; left: 318px; top: 226px; width: 452px;
    transform: scaleX(0.818); transform-origin: left top;
    font-family: "Cormorant Garamond", serif; font-weight: 500; font-size: 18px; line-height: 22px; color: var(--paper);
  }
  .front-copy span { display: block; white-space: nowrap; text-align: justify; text-align-last: justify; }
  .front-copy span.end { text-align-last: left; }

  .card-back {
    position: absolute; left: 241px; top: 628px; width: 711px; height: 538px;
    background: var(--paper); border: 1px solid #333;
  }
  .back-header {
    position: absolute; left: 0; top: 0; width: 350px; height: 93px; overflow: hidden;
    background: radial-gradient(ellipse at 50% 40%, var(--leather-mid), var(--leather-dark) 80%);
  }
  .back-header .brand { left: 24px; top: 26px; gap: 8px; }
  .back-header .brand .brand-square { width: 42px; height: 42px; }
  .back-header .brand .brand-text { width: 264px; }
  .back-header .brand .brand-name { font-size: 24px; letter-spacing: .8px; }
  .back-header .brand .brand-byline { font-size: 7.2px; letter-spacing: .8px; }
  .back-header .brand .brand-inc { font-size: 10px; }

  .back-message {
    position: absolute; left: 0; top: 98px; width: 338px; text-align: center;
    font-family: "Libre Baskerville", serif; color: var(--ink);
  }
  .back-message .contact { font-size: 15px; line-height: 19.3px; }
  .back-message .pitch { font-size: 19px; line-height: 25px; margin-top: 28px; }
  .back-message .call { font-size: 19px; line-height: 25px; margin-top: 25px; }

  .divider { position: absolute; left: 354px; top: 85px; width: 1px; height: 420px; background: var(--rule); }
  .stamp-box { position: absolute; left: 602px; top: 23px; width: 88px; height: 99px; border: 1px solid var(--rule); }
  .address-line { position: absolute; left: 388px; width: 270px; height: 1px; background: var(--rule); }
</style>
</head>
<body>
<div class="canvas">
  <div class="side-label front-label">front</div>

  <section class="card-front">
    <svg class="portrait-art" width="711" height="551" viewBox="0 0 711 551">
      <defs>
        <linearGradient id="portraitTone" x1="0" y1="0" x2="1" y2="1">
          <stop offset="0" stop-color="#7a7a78"/>
          <stop offset="0.55" stop-color="#4a4a4a"/>
          <stop offset="1" stop-color="#262626"/>
        </linearGradient>
      </defs>
      <path role="img" aria-label="Portrait photo of the firm's principal in a dark suit, arms crossed"
            d="M0,0 H232 C305,120 312,390 20,551 H0 Z" fill="url(#portraitTone)"/>
      <path d="M232,0 C305,120 312,390 20,551" fill="none" stroke="var(--brand-orange)" stroke-width="6"/>
      <path d="M250,0 C330,120 336,405 58,551" fill="none" stroke="var(--brand-blue)" stroke-width="6"/>
    </svg>

    <div class="brand">
      <div class="brand-square"></div>
      <div class="brand-text">
        <div class="brand-name">R. DESMOND PLORK</div>
        <div class="brand-inc">INC</div>
        <div class="brand-byline">TAX SUPPORT SERVICES FOR PUBLIC ACCOUNTING FIRMS</div>
      </div>
    </div>

    <h1 class="front-headline">Do your clients need help with their U.S. taxes?</h1>

    <div class="front-copy">
      <span>You probably know that U.S. citizens have to file U.S. tax</span>
      <span>returns every year—even if they live in Canada. So do your</span>
      <span>clients. That’s why they’re asking you if you know anyone</span>
      <span class="end">who can help them with their U.S. filings.</span>
      <span>Finding a tax accountant who can help with U.S. filings is</span>
      <span>tough. U.S. tax preparers have to be registered with the</span>
      <span>IRS to be eligible to prepare U.S. returns. Your client needs</span>
      <span>someone with experience, someone timely, someone</span>
      <span>charging a reasonable price. With a proven track record of</span>
      <span class="end">over 15 years, I can deliver.</span>
      <span>Feel free to pass along my contact information to your</span>
      <span class="end">clients. I’d be glad to chat.</span>
    </div>
  </section>

  <div class="side-label back-label">back</div>

  <section class="card-back">
    <div class="back-header">
      <div class="brand">
        <div class="brand-square"></div>
        <div class="brand-text">
          <div class="brand-name">R. DESMOND PLORK</div>
          <div class="brand-inc">INC</div>
          <div class="brand-byline">TAX SUPPORT SERVICES FOR PUBLIC ACCOUNTING FIRMS</div>
        </div>
      </div>
    </div>

    <div class="back-message">
      <div class="contact">
        418 Harbourview Road, Suite 9<br>
        Bayfield, NS&nbsp; B4C 2X7<br>
        Fax: (902) 555-0144<br>
        desmond@plorktax.services<br>
        www.plorktax.services
      </div>
      <p class="pitch">Do your clients need help with<br>their U.S. taxes?</p>
      <p class="call">Call US!!<br>Phone: (902) 555-0172</p>
    </div>

    <div class="divider"></div>
    <div class="stamp-box"></div>
    <div class="address-line" style="top:327px"></div>
    <div class="address-line" style="top:380px"></div>
    <div class="address-line" style="top:434px"></div>
  </section>
</div>
</body>
</html>
```